1 Page for Computer Repair Website

Looking for a 1 page website with a design that compliments the business card and pamphlet that have already been made (attached files). It should look business professional and easy to read. Email and phone number should be somewhere near the top of the website, visible when the page loads. I don't want any forms for people to mess with. No "Contact Us" form or entering in email for newsletter. Customers will just be looking at this site to confirm we are professionals and have our business in order.

Target Market(s)

Home and small business

Industry/Entity Type

Computer Repair

Coding

Coded - Design and coding required

Number of Pages Required

1 page

Font styles to use
Other font styles liked:
• Helvetica variations used in pamphlet and card

Colors
0455a3
cfdeed
85abd2
3276b5
85cae6
ffffff

Requirements
Must have
• Compliment the pamphlet and business card in color choices and font use. Pleasing to the eye and easy to read through categories and text.
Should not have
• Forms. No "enter name and email here" or anything of the sort.

```html
<!DOCTYPE html>
<html lang="en">
<head>
<meta charset="utf-8">
<title>ByteMend Computer Repair</title>
<link rel="stylesheet" href="https://fonts.googleapis.com/css2?family=Open+Sans:ital,wght@0,300;0,400;0,600;1,300&display=swap">
<style>
:root{
  --blue:#0455a3;
  --blue-mid:#3276b5;
  --sky:#1ea0dc;
  --sky-soft:#85cae6;
  --pale:#cfdeed;
  --ink:#333;
  --muted:#777;
  --band:#b9b9b9;
  --light:#f3f3f3;
  --lilac:#c9a2cf;
  --white:#fff;
  --dark:#3a3a3a;
}
*{box-sizing:border-box;margin:0;padding:0}
html,body{width:1200px;height:3788px;overflow:hidden}
body{font-family:"Open Sans",Helvetica,Arial,sans-serif;color:var(--ink);background:var(--white);position:relative}
section,header,footer{position:absolute;left:0;width:1200px}
.small{font-size:13px;line-height:22px;color:var(--muted)}
.center{text-align:center}
.section-title{font-weight:300;font-size:40px;letter-spacing:1px;text-align:center;color:#444}
.rule{width:60px;height:2px;background:var(--sky);margin:14px auto 20px}
.scroll-dot{position:absolute;right:20px;width:34px;height:34px;border-radius:50%;background:var(--dark)}
.scroll-dot svg{display:block;margin:11px auto}

.site-header{top:0;height:80px;border-bottom:1px solid #eee}
.brand{position:absolute;left:40px;top:22px;font-size:28px;font-weight:600;color:var(--blue);display:flex;align-items:center;gap:10px}
.brand i{width:14px;height:14px;background:var(--sky);display:block}
.nav{position:absolute;right:40px;top:32px;display:flex;gap:26px;font-size:11px;font-weight:600;letter-spacing:1px;color:var(--sky)}
.nav .caps{text-transform:uppercase}

.hero{top:80px;height:480px}
.hero h1{position:absolute;top:140px;width:100%;text-align:center;font-weight:300;font-size:46px;line-height:58px;color:#333}
.hero p{position:absolute;top:290px;left:200px;width:800px;text-align:center}

.services{top:560px;height:540px}
.services .intro{width:1000px;margin:0 auto}
.service-grid{display:flex;justify-content:center;gap:40px;margin-top:40px}
.service{width:230px;text-align:center}
.service .thumb{width:80px;height:80px;margin:0 auto 20px;background:linear-gradient(135deg,#8a8a8a,#6e6e6e)}
.service h3{font-size:16px;font-weight:400;margin-bottom:12px;color:#444}

.quote{top:1100px;height:290px;background:var(--band);color:var(--white);text-align:center}
.quote blockquote{margin:100px auto 0;width:900px;font-size:26px;font-style:italic;font-weight:300;line-height:36px}
.quote cite{display:block;margin-top:24px;font-size:13px;font-style:normal;color:var(--blue)}

.about{top:1390px;height:540px}
.about .intro{width:1000px;margin:0 auto}
.features{position:absolute;top:250px;left:60px;width:520px}
.feature{display:flex;align-items:center;justify-content:flex-end;gap:24px;margin-bottom:34px;text-align:right}
.feature h4{font-size:14px;font-weight:400;color:#444;margin-bottom:4px}
.feature .icon{flex:none;width:54px;height:54px;border:1px solid var(--pale);border-radius:50%;display:flex;align-items:center;justify-content:center}
.about .photo{position:absolute;top:250px;left:620px;width:520px;height:260px;background:linear-gradient(135deg,#d7d7d7,#c6c6c6)}

.work{top:1930px;height:640px;background:var(--light)}
.work .photo{position:absolute;top:170px;left:60px;width:520px;height:420px;background:linear-gradient(135deg,#9a9a9a,#7d7d7d)}
.work .detail{position:absolute;top:170px;left:600px;width:540px}
.work h3{font-size:18px;font-weight:400;margin-bottom:10px;color:#444}
.work h5{font-size:11px;font-weight:600;text-transform:uppercase;color:#555;margin-top:10px}

.reach{top:2570px;height:140px;background:var(--lilac)}
.reach .text{position:absolute;left:60px;top:38px;width:520px;font-size:13px;color:var(--blue);line-height:20px}
.reach .text strong{display:block;text-transform:uppercase;font-size:13px;color:var(--blue)}
.reach .direct{position:absolute;left:600px;top:50px;width:540px;height:40px;display:flex;gap:10px}
.reach .direct span{flex:1;background:var(--white);font-size:13px;color:var(--blue);line-height:40px;text-align:center}
.reach .direct span.strong{background:var(--sky);color:var(--white);font-weight:600}

.contact{top:2710px;height:790px}
.contact .map{position:absolute;top:210px;left:0;width:1200px;height:570px;background:linear-gradient(160deg,#eee6f2,#dccbe6 60%,#e9dfee)}

.footer{top:3500px;height:288px;background:var(--light)}
.hours{position:absolute;left:60px;top:40px;width:760px}
.hours h6,.info h6{font-size:11px;font-weight:600;text-transform:uppercase;color:#555;margin-bottom:10px}
.hours-row{display:flex;justify-content:space-between;height:40px;background:var(--white);border:1px solid #e3e3e3;padding:0 14px;margin-bottom:10px;font-size:13px;line-height:38px;color:var(--muted)}
.hours-row b{font-weight:600;color:#555}
.info{position:absolute;left:860px;top:40px;width:280px}
.info .line{display:flex;align-items:center;gap:10px}
.socials{display:flex;gap:10px;margin-top:6px}
.socials span{width:22px;height:22px;border-radius:50%;background:#ccc}
</style>
</head>
<body>

<header class="site-header">
  <div class="brand"><i></i>ByteMend</div>
  <nav class="nav">
    <span class="caps">Our Services</span><span>hello@bytemend.example</span><span class="caps">About Us</span><span class="caps">Contact Us</span><span>555-0148</span>
  </nav>
</header>

<section class="hero">
  <h1>PC/Laptop<br>Hardware Repair</h1>
  <p class="small">Our certified technicians work fast on every machine. We can repair or upgrade the parts you use most and keep your home or office running. Bring in the desktop or laptop that has slowed down, and leave with a system that feels new again.</p>
</section>

<section class="services">
  <h2 class="section-title">OUR SERVICES</h2>
  <div class="rule"></div>
  <p class="small center intro">Our certified technicians handle repairs for home and small business. We diagnose faults, replace parts and upgrade systems so your computer runs reliably again, with clear pricing and fast turnaround.</p>
  <div class="service-grid">
    <div class="service"><div class="thumb" role="img" aria-label="Malware removal image"></div><h3>Malware Removal</h3><p class="small">We remove viruses, spyware and adware, then secure the system so it stays clean and safe for everyday use.</p></div>
    <div class="service"><div class="thumb" role="img" aria-label="Data migration image"></div><h3>Data Migration</h3><p class="small">Move files, photos and settings to a new machine without loss, handled carefully from start to finish.</p></div>
    <div class="service"><div class="thumb" role="img" aria-label="Clean and tune up image"></div><h3>Clean / Tune Ups</h3><p class="small">Dust removal, fresh thermal paste and software cleanup restore speed and keep your system cool.</p></div>
    <div class="service"><div class="thumb" role="img" aria-label="Remote support image"></div><h3>Remote Support</h3><p class="small">Quick fixes over a secure remote session, so small problems are solved without leaving your desk.</p></div>
  </div>
  <div class="scroll-dot" style="top:120px"><svg width="12" height="12" viewBox="0 0 12 12"><path d="M2 8l4-4 4 4" stroke="#fff" stroke-width="2" fill="none"/></svg></div>
</section>

<section class="quote">
  <blockquote>Fast, honest and professional service. My office computers were back up the same day, and everything was explained in plain words.</blockquote>
  <cite>Daniel Reyes</cite>
  <div class="scroll-dot" style="top:228px"><svg width="12" height="12" viewBox="0 0 12 12"><path d="M2 8l4-4 4 4" stroke="#fff" stroke-width="2" fill="none"/></svg></div>
</section>

<section class="about">
  <h2 class="section-title" style="margin-top:110px">ABOUT US</h2>
  <div class="rule"></div>
  <p class="small center intro">We are a local repair team serving homes and small businesses. Every job is handled by trained technicians who care about your data, your time and a fair price.</p>
  <div class="features">
    <div class="feature"><div><h4>Top Services</h4><p class="small">Repairs, upgrades and setup done right the first time.</p></div><div class="icon"><svg width="22" height="22" viewBox="0 0 24 24"><path d="M12 2l3 7h7l-5.5 4.5L18.5 21 12 16.5 5.5 21l2-7.5L2 9h7z" fill="none" stroke="#1ea0dc" stroke-width="1.5"/></svg></div></div>
    <div class="feature"><div><h4>CORE VALUES</h4><p class="small">Honest advice, clear quotes and respect for your privacy.</p></div><div class="icon"><svg width="22" height="22" viewBox="0 0 24 24"><path d="M12 21s-8-5-8-11a4.5 4.5 0 018-3 4.5 4.5 0 018 3c0 6-8 11-8 11z" fill="none" stroke="#1ea0dc" stroke-width="1.5"/></svg></div></div>
    <div class="feature"><div><h4>DATA PRIVACY</h4><p class="small">Your files stay secure and confidential at every step.</p></div><div class="icon"><svg width="22" height="22" viewBox="0 0 24 24"><circle cx="12" cy="8" r="4" fill="none" stroke="#1ea0dc" stroke-width="1.5"/><path d="M4 21c0-4 4-6 8-6s8 2 8 6" fill="none" stroke="#1ea0dc" stroke-width="1.5"/></svg></div></div>
  </div>
  <div class="photo" role="img" aria-label="Photo of the repair team at work"></div>
</section>

<section class="work">
  <h2 class="section-title" style="margin-top:60px">ABOUT OUR Services</h2>
  <p class="small center" style="margin-top:8px">Here are just a few of the problems we fix on desktops and laptops.</p>
  <div class="photo" role="img" aria-label="Photo of a computer being repaired"></div>
  <div class="detail">
    <h3>Computer Repair</h3>
    <p class="small">From failed drives to broken screens, we find the fault and fix it with quality parts and clear pricing.</p>
    <h5>Fix Computer</h5><p class="small">Startup errors and crashes</p>
    <h5>Upgrade</h5><p class="small">Memory and storage</p>
    <h5>Network</h5><p class="small">Wi-Fi and office setup</p>
    <h5>Backup</h5><p class="small">Cloud and local copies</p>
    <h5>Cleanup</h5><p class="small">Speed and startup items</p>
    <h5>Consultation</h5><p class="small">Advice on new purchases</p>
    <p class="small" style="margin-top:10px">Every repair includes a full test before pickup, so you leave with a machine that works as it should.</p>
  </div>
  <div class="scroll-dot" style="top:50px"><svg width="12" height="12" viewBox="0 0 12 12"><path d="M2 8l4-4 4 4" stroke="#fff" stroke-width="2" fill="none"/></svg></div>
</section>

<section class="reach">
  <div class="text"><strong>Talk to a technician today</strong>Call or email us and we will answer the same business day.</div>
  <div class="direct"><span>hello@bytemend.example</span><span class="strong">555-0148</span></div>
</section>

<section class="contact">
  <h2 class="section-title" style="margin-top:100px">GET IN TOUCH WITH US</h2>
  <p class="small center" style="margin-top:10px">A question, contact us on our working hours: Monday to Friday, 9am to 6pm.</p>
  <div class="map" role="img" aria-label="Street map showing the shop location"></div>
  <div class="scroll-dot" style="top:110px"><svg width="12" height="12" viewBox="0 0 12 12"><path d="M2 8l4-4 4 4" stroke="#fff" stroke-width="2" fill="none"/></svg></div>
</section>

<footer class="footer">
  <div class="hours">
    <h6>Opening Hours</h6>
    <div class="hours-row"><b>Monday – Friday</b><span>9:00am – 6:00pm</span></div>
    <div class="hours-row"><b>Saturday</b><span>10:00am – 2:00pm</span></div>
    <div class="hours-row"><b>Sunday</b><span>Closed</span></div>
    <div class="hours-row"><b>Remote Support</b><span>By appointment</span></div>
  </div>
  <div class="info">
    <h6>Contact Info</h6>
    <p class="small">Local repair team for home and small business. Fast service and clear pricing.</p>
    <p class="small line" style="margin-top:6px"><svg width="12" height="12" viewBox="0 0 24 24"><path d="M12 2a7 7 0 00-7 7c0 5 7 13 7 13s7-8 7-13a7 7 0 00-7-7z" fill="#1ea0dc"/></svg>120 Harbor Lane, Springfield</p>
    <p class="small line"><svg width="12" height="12" viewBox="0 0 24 24"><path d="M6 2l4 4-2 3a12 12 0 007 7l3-2 4 4-3 4C10 22 2 14 2 5z" fill="#1ea0dc"/></svg>555-0148</p>
    <p class="small line"><svg width="12" height="12" viewBox="0 0 24 24"><rect x="2" y="5" width="20" height="14" fill="none" stroke="#1ea0dc" stroke-width="2"/><path d="M2 5l10 8 10-8" fill="none" stroke="#1ea0dc" stroke-width="2"/></svg>hello@bytemend.example</p>
    <h6 style="margin-top:12px">Follow Us</h6>
    <div class="socials"><span></span><span></span><span></span><span></span><span></span></div>
  </div>
</footer>

</body>
</html>
```